Business Card Design Project

New Business Card design for Varodine Technology Ltd using new Logo and new Tagline for staffing company.

About us from our website - www.varodine.example:

VaroDine is a leading and recognized Electronic Entertainment, Workforce Augmentation, and Project Management solutions provider with clients in Electronic Entertainment, Legal, Technology, Government and other verticals that range in size from start up organizations to Zenlar 500 companies. VaroDine is certified as an 8(a) minority and woman owned enterprise, established in 1998.

Target Market(s)

Companies in Electronic Entertainment, Legal, Government and Technology

Industry/Entity Type

Business

Requirements
Must have
• Must include in small letters the following information on back:

Established in 1998
8(a)(w)(e), Cage #7KRT9, DUNS #462137580

Front should have the following:
Derek Holloway
Vice President
5820 Birchmont Road
Fallowby, FB 482917
555-318-2746 X 100
555-902-6613 Fax
555-318-2746 Toll Free
name@varodine.example

Our Tagline: Connect • Collaborate • Achieve

```html
<!DOCTYPE html>
<html lang="en">
<head>
<meta charset="utf-8">
<title>VaroDine Business Card</title>
<link rel="stylesheet" href="https://fonts.googleapis.com/css2?family=Questrial&family=Cormorant+SC:wght@500&display=swap">
<style>
  :root {
    --page-bg: #ffffff;
    --card-dark-top: #45484d;
    --card-dark-bottom: #0f1012;
    --card-light-top: #ffffff;
    --card-light-bottom: #c9cacc;
    --ink-white: #ffffff;
    --ink-blue: #1f5fa8;
    --ink-logo: #55585d;
    --ink-faint: #5d6066;
  }
  * { box-sizing: border-box; margin: 0; padding: 0; }
  html, body { width: 1200px; height: 900px; overflow: hidden; background: var(--page-bg); }
  .canvas { position: relative; width: 1200px; height: 900px; }
  .card {
    position: absolute; left: 348px; width: 516px; height: 344px; overflow: hidden;
    font-family: "Questrial", "Century Gothic", sans-serif;
  }
  .card-front { top: 104px; background: linear-gradient(to bottom, var(--card-dark-top), var(--card-dark-bottom)); }
  .card-back {
    top: 484px;
    background: linear-gradient(to bottom, var(--card-light-top) 0%, var(--card-light-bottom) 38%, var(--card-dark-top) 38%, var(--card-dark-bottom) 100%);
  }
  .contact { position: absolute; right: 36px; top: 30px; text-align: right; }
  .contact-name { color: var(--ink-white); font-size: 23px; line-height: 1; }
  .contact-title { color: var(--ink-white); font-size: 14px; margin-top: 5px; }
  .contact-address { color: var(--ink-blue); font-size: 15px; line-height: 17px; margin-top: 22px; }
  .contact-lines { list-style: none; color: var(--ink-blue); font-size: 16px; margin-top: 26px; }
  .contact-lines li { height: 31px; }
  .front-mark {
    position: absolute; left: 4px; bottom: 8px; color: var(--ink-faint); opacity: 0.55;
    font-size: 74px; line-height: 1; letter-spacing: -1px;
  }
  .brand { position: absolute; left: 0; right: 0; top: 66px; display: flex; justify-content: center; align-items: center; gap: 14px; }
  .brand-dot { width: 22px; height: 22px; border-radius: 50%; background: var(--ink-blue); }
  .brand-name { color: var(--ink-logo); font-size: 64px; line-height: 1; letter-spacing: -1px; }
  .back-text { position: absolute; left: 0; right: 0; text-align: center; color: var(--ink-white); }
  .tagline { top: 210px; font-family: "Cormorant SC", "Trajan Pro", serif; font-size: 23px; letter-spacing: 1px; }
  .established { top: 252px; font-family: "Cormorant SC", "Trajan Pro", serif; font-size: 22px; letter-spacing: 1px; }
  .credentials { top: 296px; font-size: 12px; }
</style>
</head>
<body>
<main class="canvas">
  <section class="card card-front" aria-label="Card front">
    <div class="front-mark" aria-hidden="true">VaroDine</div>
    <div class="contact">
      <p class="contact-name">Derek Holloway</p>
      <p class="contact-title">Vice President</p>
      <p class="contact-address">5820 Birchmont Road<br>Fallowby, FB 482917</p>
      <ul class="contact-lines">
        <li>555-318-2746 X 100</li>
        <li>555-902-6613 Fax</li>
        <li>555-318-2746 Toll Free</li>
        <li>name@varodine.example</li>
      </ul>
    </div>
  </section>

  <section class="card card-back" aria-label="Card back">
    <div class="brand">
      <span class="brand-dot"></span>
      <span class="brand-name">VaroDine</span>
    </div>
    <p class="back-text tagline">Connect • Collaborate • Achieve</p>
    <p class="back-text established">Established in 1998</p>
    <p class="back-text credentials">8(a)(w)(e), Cage #7KRT9, DUNS #462137580</p>
  </section>
</main>
</body>
</html>
```